Postcard Design

I am a speech pathologist. My company is called Bramble Hop. I have a program called "Quiet Paws" to help children stop sucking their thumb/ fingers. After they complete the program, I need to check in after 6 months to make sure they have continued with their success, and to see if they may be ready for the follow up program "Lark Loops" for those with a tongue thrust.

On one side, I would like "Bramble Hop....Quiet paws to your success!" with my logo. On the other side, I would like a reflective sticker like a mirror that says something like "Bramble hop...it's time to check your smile". Please contact Harriet if you think a Tongue thrust may be present. Lark Loops is a follow up program to retrain the tongue to work properly in the mouth. Please discuss with your orthodontist/ dentist or contact Harriet if you want to schedule an evaluation.
Updates

Reason: Just trying to make sure I get the best postcard as possible. I've extended the deadline by a few days to see what else comes in and to tweak the changes I've already received. Thanks!

Target Market(s)

families and children

Industry/Entity Type

It Company

Requirements
Must have
• logos for Bramble Hop, Quiet Paws, and Lark Loops
Nice to have
• I had this idea of a paper reflective mirror for the back so the children can actually see their smile when they look in it, but know that may be impossible. Just a creative idea.

```html
<!DOCTYPE html>
<html lang="en">
<head>
<meta charset="utf-8">
<title>Bramble Hop – Postcard</title>
<link href="https://fonts.googleapis.com/css2?family=Quicksand:wght@500;600;700&family=Open+Sans:wght@600;700&display=swap" rel="stylesheet">
<style>
  :root {
    --page: #eceae6;
    --card: #ffffff;
    --blue: #3f7fbf;
    --blue-soft: #a9c1e3;
    --blue-pale: #dfe8f5;
    --orange: #f08a1c;
    --ink: #2b4f86;
    --line: #c9cfd8;
    --silver-1: #f4f5f6;
    --silver-2: #c9ccd0;
  }
  * { box-sizing: border-box; margin: 0; padding: 0; }
  html, body { width: 1200px; height: 900px; overflow: hidden; }
  body {
    background: var(--page);
    position: relative;
    font-family: "Quicksand", sans-serif;
    color: var(--ink);
  }

  .card {
    position: absolute;
    background: var(--card);
    box-shadow: 0 6px 18px rgba(0,0,0,.18);
    overflow: hidden;
  }

  /* ---------- back side ---------- */
  .card--back { left: 24px; top: 24px; width: 620px; height: 400px; }
  .card--back .top-swoosh { position: absolute; left: 0; top: 0; width: 100%; height: 80px; }
  .stamp-box {
    position: absolute; right: 34px; top: 18px;
    width: 112px; height: 128px; border: 1.5px solid var(--line);
  }
  .brand {
    position: absolute; display: flex; align-items: center; gap: 8px;
    font-family: "Quicksand", sans-serif; font-weight: 700; color: var(--blue);
    white-space: nowrap;
  }
  .brand__dot { width: 11px; height: 11px; border-radius: 50%; background: var(--orange); flex: none; }
  .card--back .brand { left: 22px; top: 100px; font-size: 28px; line-height: 1; }
  .contact {
    position: absolute; font-family: "Quicksand", sans-serif; font-weight: 700;
    display: flex; flex-direction: column; gap: 3px; white-space: nowrap;
  }
  .contact__row { display: flex; align-items: center; gap: 6px; }
  .contact__row svg { width: 12px; height: 12px; flex: none; }
  .card--back .contact {
    left: 248px; top: 88px; padding-left: 10px; border-left: 1.5px solid var(--blue);
    color: var(--blue); font-size: 14px;
  }
  .banner {
    position: absolute; background: var(--blue); color: #fff;
    font-family: "Open Sans", sans-serif; font-weight: 700; white-space: nowrap;
  }
  .card--back .banner {
    left: 10px; top: 138px; width: 400px; height: 28px; font-size: 19px;
    padding: 1px 0 0 22px;
  }
  .message {
    position: absolute; left: 22px; top: 176px; width: 318px;
    font-size: 13px; line-height: 16.5px; font-weight: 600; color: var(--ink);
  }
  .program-mark { position: absolute; left: 150px; top: 348px; text-align: center; }
  .program-mark__name {
    display: flex; align-items: center; justify-content: center; gap: 6px;
    font-weight: 700; font-size: 21px; line-height: 1.1; color: var(--blue); letter-spacing: .5px;
  }
  .program-mark__name .square { width: 10px; height: 10px; background: var(--orange); }
  .program-mark__tag { font-size: 7px; font-weight: 600; color: var(--blue); letter-spacing: .4px; }
  .address-lines { position: absolute; left: 355px; top: 200px; width: 235px; }
  .address-lines span { display: block; height: 40px; border-bottom: 1.5px solid var(--line); }

  /* ---------- front side ---------- */
  .card--front {
    left: 560px; top: 444px; width: 610px; height: 432px;
    background: linear-gradient(180deg, var(--blue-pale) 0%, #eef3fa 55%, var(--blue-soft) 100%);
  }
  .photo-area {
    position: absolute; right: 0; top: 0; width: 265px; height: 400px;
    background: linear-gradient(160deg, #e9ecf1 0%, #c9b8a8 40%, #8f6a55 70%, #b6524c 100%);
  }
  .front-curves { position: absolute; inset: 0; width: 100%; height: 100%; }
  .card--front .brand { left: 26px; top: 62px; font-size: 31px; line-height: 1; }
  .card--front .banner--head {
    left: 10px; top: 108px; width: 322px; height: 30px; font-size: 17.5px; padding: 3px 0 0 30px;
  }
  .mirror {
    position: absolute; left: 30px; top: 138px; width: 288px; height: 262px;
    background: linear-gradient(135deg, var(--silver-1), var(--silver-2) 55%, #eef0f2);
    border: 2.5px solid var(--blue);
    border-radius: 50% 50% 50% 50% / 55% 55% 45% 45%;
  }
  .badge {
    position: absolute; left: 22px; top: 150px; width: 96px; height: 96px;
    border-radius: 50%; background: #fff; border: 3px solid var(--orange);
    display: flex; align-items: center; justify-content: center;
    font-weight: 700; font-size: 15px; color: var(--blue);
  }
  .check-label {
    position: absolute; left: 280px; top: 360px; transform: rotate(-72deg); transform-origin: left top;
    font-family: "Open Sans", sans-serif; font-weight: 700; font-size: 10.5px; color: var(--blue);
    white-space: nowrap;
  }
  .check-label em { font-style: normal; color: var(--orange); }
  .card--front .banner--foot {
    left: 10px; top: 386px; width: 320px; height: 26px; font-size: 16.5px; padding: 1px 0 0 46px;
  }
  .card--front .contact { left: 368px; top: 368px; font-size: 15px; color: #fff; }
</style>
</head>
<body>

  <section class="card card--back">
    <svg class="top-swoosh" viewBox="0 0 620 80" preserveAspectRatio="none" aria-hidden="true">
      <path d="M0 0 H470 Q250 10 0 64 Z" fill="#dfe8f5"/>
      <path d="M0 64 Q250 10 470 0" fill="none" stroke="#3f7fbf" stroke-width="3"/>
    </svg>
    <div class="stamp-box"></div>

    <div class="brand"><span class="brand__dot"></span>Bramble Hop</div>
    <div class="contact">
      <div class="contact__row">
        <svg viewBox="0 0 12 12"><path d="M2.5 1 L4.5 1 L5 3.6 L3.8 4.6 Q5 7 7.4 8.2 L8.4 7 L11 7.5 L11 9.5 Q11 11 9.5 11 Q1 10 1 2.5 Q1 1 2.5 1Z" fill="#f08a1c"/></svg>
        555-013-2470
      </div>
      <div class="contact__row">
        <svg viewBox="0 0 12 12"><rect x="0.8" y="2.2" width="10.4" height="7.6" fill="none" stroke="#f08a1c" stroke-width="1.3"/><path d="M1 2.6 L6 6.6 L11 2.6" fill="none" stroke="#f08a1c" stroke-width="1.3"/></svg>
        hello@bramblehop.example
      </div>
    </div>

    <div class="banner">it's time to check your smile</div>

    <p class="message">Now that your child has eliminated their thumb/ finger sucking habit, it is time to check in and make sure there is not a residual tongue thrust. A tongue thrust is the incorrect posture of the tongue during speech, swallowing, or at rest. A tongue thrust can cause a change in the alignment of your teeth, even with orthodontic treatment. The Lark Loops program is a short term therapy program with long term results. If you think your child may have a tongue thrust, please contact Harriet for an evaluation.</p>

    <div class="program-mark">
      <div class="program-mark__name">LARK LOOPS<span class="square"></span></div>
      <div class="program-mark__tag">A TONGUE THRUST REMEDIATION PROGRAM</div>
    </div>

    <div class="address-lines"><span></span><span></span><span></span><span></span></div>
  </section>

  <section class="card card--front">
    <div class="photo-area" role="img" aria-label="Photo of a smiling young child in a striped shirt"></div>
    <svg class="front-curves" viewBox="0 0 610 432" preserveAspectRatio="none" aria-hidden="true">
      <path d="M0 40 Q300 0 610 14" fill="none" stroke="#ffffff" stroke-width="4"/>
      <path d="M0 50 Q300 10 610 22" fill="none" stroke="#3f7fbf" stroke-width="2"/>
      <path d="M345 432 L345 400 Q480 380 610 290 L610 432 Z" fill="#6f96cf"/>
      <path d="M0 400 Q320 420 610 300" fill="none" stroke="#ffffff" stroke-width="3"/>
      <path d="M0 412 Q320 432 610 318" fill="none" stroke="#3f7fbf" stroke-width="2"/>
    </svg>

    <div class="brand"><span class="brand__dot"></span>Bramble Hop</div>
    <div class="banner banner--head">It's time to check on your smile</div>

    <div class="mirror" role="img" aria-label="Reflective mirror sticker"></div>
    <div class="badge">Quiet Paws</div>
    <div class="check-label"><em>check</em> your smile!!</div>

    <div class="banner banner--foot">Quiet paws to your success!</div>

    <div class="contact">
      <div class="contact__row">
        <svg viewBox="0 0 12 12"><path d="M2.5 1 L4.5 1 L5 3.6 L3.8 4.6 Q5 7 7.4 8.2 L8.4 7 L11 7.5 L11 9.5 Q11 11 9.5 11 Q1 10 1 2.5 Q1 1 2.5 1Z" fill="#f08a1c"/></svg>
        555-013-2470
      </div>
      <div class="contact__row">
        <svg viewBox="0 0 12 12"><rect x="0.8" y="2.2" width="10.4" height="7.6" fill="none" stroke="#f08a1c" stroke-width="1.3"/><path d="M1 2.6 L6 6.6 L11 2.6" fill="none" stroke="#f08a1c" stroke-width="1.3"/></svg>
        hello@bramblehop.example
      </div>
    </div>
  </section>

</body>
</html>
```